I need a certificate for print - for completion of a course

I need someone to design for me a certificate printable on 8.5 x 11" card stock paper.

The design is for a permanent makeup course. I have attached my own certificate for an example. I am not 100% happy with my design, but the verbiage must stay the same.

I have also attached other certificates that I really like from other companies.

I want this certificate to be special. The colors for my company is pink and white. www.lashverde.example

Target Market(s)

beauty industry

Industry/Entity Type

Makeup

Requirements
Must have
• Beautiful imagery. Pink and white

```html
<!DOCTYPE html>
<html lang="en">
<head>
<meta charset="UTF-8">
<title>Certified Microblading Artist – Lash Verde Academy</title>
<link rel="stylesheet" href="https://fonts.googleapis.com/css2?family=Jost:wght@300;400;500&family=Oswald:wght@600&family=Tinos:wght@700&display=swap">
<style>
  :root {
    --bg-dark: #1d1e22;
    --bg-mid: #3a3b40;
    --bg-light: #4a4b50;
    --brand-pink: #ee7fb6;
    --text-pink: #f4c6e0;
    --title-yellow: #fff200;
    --white: #ffffff;
    --rule: #d8d8dc;
    --border-violet: #6f5fa8;
    --seal-mint: #d9eadb;
    --skin-light: #e9d2c8;
    --skin-mid: #c79a8c;
    --hair-dark: #24201f;
  }
  * { margin: 0; padding: 0; box-sizing: border-box; }
  html, body {
    width: 1200px;
    height: 934px;
    overflow: hidden;
    background: var(--bg-dark);
  }
  .certificate {
    position: relative;
    width: 1200px;
    height: 934px;
    overflow: hidden;
    background: radial-gradient(ellipse at 40% 30%, var(--bg-light) 0%, var(--bg-mid) 35%, var(--bg-dark) 85%);
    font-family: "Jost", sans-serif;
  }
  .side-border {
    position: absolute;
    left: 0; top: 0;
    width: 50px; height: 934px;
    background: linear-gradient(90deg, #8a7cc0 0%, var(--border-violet) 45%, rgba(60,55,90,0.6) 100%);
  }
  .portrait {
    position: absolute;
    left: 540px; top: 0;
    width: 660px; height: 934px;
    background:
      linear-gradient(90deg, rgba(42,43,48,1) 0%, rgba(42,43,48,0) 30%),
      linear-gradient(180deg, var(--hair-dark) 0%, rgba(36,32,31,0.85) 18%, rgba(36,32,31,0) 32%),
      linear-gradient(90deg, rgba(40,40,44,1) 0%, rgba(40,40,44,0.4) 22%, var(--skin-mid) 48%, var(--skin-light) 75%, var(--skin-mid) 100%);
  }
  .watermark-area {
    position: absolute;
    left: 90px; top: 310px;
    width: 560px; height: 480px;
    border-radius: 50%;
    background: rgba(110,100,170,0.08);
  }
  .brand {
    position: absolute;
    left: 100px; top: 138px;
    white-space: nowrap;
    font-family: "Jost", sans-serif;
    font-weight: 400;
    font-size: 50px;
    line-height: 1;
    color: var(--brand-pink);
  }
  .title {
    position: absolute;
    left: 66px; top: 266px;
    white-space: nowrap;
    font-family: "Oswald", sans-serif;
    font-weight: 600;
    font-size: 36px;
    line-height: 1.1;
    color: var(--title-yellow);
  }
  .intro {
    position: absolute;
    left: 62px; top: 398px;
    font-weight: 300;
    font-size: 28px;
    line-height: 32px;
    color: var(--text-pink);
  }
  .recipient {
    position: absolute;
    left: 62px; top: 436px;
    width: 566px;
    padding-bottom: 2px;
    border-bottom: 1.5px solid var(--rule);
    font-family: "Tinos", serif;
    font-weight: 700;
    font-size: 48px;
    line-height: 1.05;
    color: var(--white);
    letter-spacing: 1.5px;
  }
  .statement {
    position: absolute;
    left: 62px; top: 504px;
    white-space: nowrap;
    font-weight: 300;
    font-size: 29px;
    line-height: 35px;
    color: var(--text-pink);
  }
  .signatory {
    position: absolute;
    left: 74px; top: 840px;
    color: var(--white);
  }
  .signatory-name {
    font-weight: 500;
    font-size: 22px;
    line-height: 32px;
  }
  .signatory-role {
    font-weight: 300;
    font-size: 22px;
    line-height: 32px;
    letter-spacing: 0.8px;
  }
  .seal-box {
    position: absolute;
    left: 478px; top: 834px;
    width: 272px; height: 68px;
    background: var(--seal-mint);
  }
  .marker-dot {
    position: absolute;
    left: 846px; top: 275px;
    width: 36px; height: 36px;
    border-radius: 50%;
    background: var(--white);
  }
</style>
</head>
<body>
  <main class="certificate">
    <div class="portrait" role="img" aria-label="Close-up beauty portrait of a woman with dark fringe, defined brows and glossy red lips"></div>
    <div class="side-border" role="img" aria-label="Violet guilloche border pattern"></div>
    <div class="watermark-area" role="img" aria-label="Faint violet guilloche security pattern"></div>

    <header class="brand">Lash Verde Academy</header>

    <h1 class="title">CERTIFIED MICROBLADING ARTIST</h1>

    <p class="intro">This is to certify that</p>
    <p class="recipient">Dana Whitlock</p>
    <p class="statement">has successfully proven to be an Artist of the<br>Highest Standard in Eyebrow<br>Micropigmentation using the LASH VERDE<br>INTERNATIONAL® Microblading Method</p>

    <footer class="signatory">
      <p class="signatory-name">Clara Ruth Benning</p>
      <p class="signatory-role">Founder and Head Trainer</p>
    </footer>
    <div class="seal-box"></div>
    <div class="marker-dot"></div>
  </main>
</body>
</html>
```